Brightline Tech Partners Website Design

I have here a website mockup. If you need anything further please feel free to reach out to me! Thank you!

Current site: http://brightlinetechpartners.example/

We want it clean, concise and eye catching.

Menu: I want the same idea we used from pellaroweb.example with the logo in the middle and in the menu:

Home, About Us, How Can We Help?, Media, Blog, Contact Us.

Let's have the Social Media icons at the very top please.

For the banner - we want a imagevault chess image sort of like imagevault photo 122579353 or 77865526

I want the words "Plan Ahead, Work Smarter, Stay Strong" to come in one at a time and then "Brightline Tech Partners" to show up on the banner.

Maybe have "Grow Your Business with Managed IT Services from Brightline Tech Partners" somewhere permanently on the banner that still suits everything.

Services Section: Maybe we can have them as chess pieces with something along the lines of "Make Your Next Move" - Managed IT Services, New Jersey Cloud Computing, Protect Your Business Data, Managed Email Solutions (Background 514558306)

Next Area: What sets us apart?/Testimonials (I want this as a split area) (Can we please use the banner image paralex here?)

(This is for the What Sets Us Apart side)
Outsmart threats before they reach your networks.

Outperform with the newest and latest technologies to not only keep you up and running, but to keep you at an advantage.

Outlast by embracing Business Continuity with Brightline Tech Partners by your side. (I will let you choose the background for here!)

Next Area: Book Your Free Two-Hour Review! (I want a form similar to the one on the old site.)

Next area: Blogs/Sign Up for our newsletter! (Again, please choose a relevant background)

Next Area:Contact Us area with service pages. I really like the contact us part in dorvaly.example where it shows the geographical area.

Target Market(s)

Business Owners in New Jersey looking to outsource their business IT, computer and network support.

Industry/Entity Type

Information Technology

Number of Pages Required

1 page

Font styles to use
Sans Serif

Requirements
Must have
• We want this website to be very sharp. I like bright colors, creative imagery.
• In the footer I must have @ 2016 Brightline Tech Partners | Privacy Policy | Sitemap
Should not have
• I am not a fan of stuffing everything in and making it very busy. I would like clean and professional

```html
<!DOCTYPE html>
<html lang="en">
<head>
<meta charset="utf-8">
<title>Brightline Tech Partners – Managed IT Services</title>
<link rel="stylesheet" href="https://fonts.googleapis.com/css2?family=Roboto:wght@400;500;700&family=Kalam:wght@400;700&display=swap">
<style>
  :root {
    --topbar: #86a9d8;
    --topbar-text: #ffffff;
    --white: #ffffff;
    --ink: #1f2530;
    --link-active: #3a8fd6;
    --accent: #4a9be6;
    --hero-deep: #1b2944;
    --hero-mid: #2b3c5e;
    --hero-light: #5c6c8a;
    --icon-blue: #2a9cf0;
    --icon-deep: #1565c8;
    --icon-pale: #bfe2ff;
    --band-light: #8cb6e8;
    --band-mid: #5d9ce3;
  }
  * { box-sizing: border-box; margin: 0; padding: 0; }
  html, body { width: 1200px; height: 676px; overflow: hidden; background: var(--white); }
  body { font-family: "Roboto", Arial, sans-serif; color: var(--ink); position: relative; }

  .top-bar {
    position: absolute; left: 0; top: 0; width: 1200px; height: 32px;
    background: var(--topbar); color: var(--topbar-text);
    font-size: 12.5px; display: flex; align-items: center;
  }
  .top-bar__tagline { margin-left: 40px; }
  .top-bar__phone { margin-left: 26px; display: flex; align-items: center; gap: 6px; }
  .top-bar__tools { position: absolute; right: 42px; top: 0; height: 32px; display: flex; align-items: center; gap: 18px; }
  .social-dot { width: 9px; height: 9px; border-radius: 50%; background: var(--white); }

  .site-nav {
    position: absolute; left: 0; top: 32px; width: 1200px; height: 78px;
    background: var(--white);
  }
  .site-nav__link {
    position: absolute; top: 28px; font-size: 15px; font-weight: 500;
    color: var(--ink); text-decoration: none; letter-spacing: 0.2px;
  }
  .site-nav__link--active { color: var(--link-active); font-weight: 400; }
  .site-nav__signup {
    position: absolute; top: 26px; left: 1018px; padding: 2px 6px;
    background: var(--accent); color: var(--white); font-size: 14px; font-weight: 700;
    border-radius: 3px; text-decoration: none;
  }

  .logo-tab {
    position: absolute; left: 446px; top: 32px; width: 272px; height: 110px;
    background: var(--white); border-radius: 0 0 6px 6px; z-index: 3;
    display: flex; align-items: center; justify-content: center; gap: 8px;
    box-shadow: 0 2px 4px rgba(0,0,0,0.12);
  }
  .logo-tab__mark { width: 15px; height: 15px; border-radius: 50%; background: var(--accent); }
  .logo-tab__name { font-size: 18px; font-weight: 700; color: var(--ink); }

  .hero {
    position: absolute; left: 0; top: 110px; width: 1200px; height: 426px;
    background: radial-gradient(ellipse at 88% 15%, var(--hero-light) 0%, var(--hero-mid) 38%, var(--hero-deep) 82%);
    overflow: hidden;
  }
  .hero__globe {
    position: absolute; left: 48px; top: 6px; width: 420px; height: 420px;
    border-radius: 50%;
    background:
      radial-gradient(circle at 38% 32%, rgba(120,180,240,0.22) 0%, rgba(60,130,200,0.10) 35%, transparent 60%),
      radial-gradient(circle at 50% 50%, rgba(30,80,140,0.10) 0%, rgba(40,110,180,0.22) 72%, rgba(70,150,225,0.45) 96%, rgba(70,150,225,0) 100%);
  }
  .hero__headline {
    position: absolute; left: 700px; top: 116px; width: 460px;
    font-family: "Kalam", "Comic Sans MS", cursive; font-weight: 400;
    font-size: 36px; line-height: 55px; color: var(--white); text-align: center;
  }
  .hero__dots { position: absolute; left: 602px; top: 395px; display: flex; gap: 8px; }
  .hero__dot { width: 9px; height: 9px; border-radius: 50%; background: var(--white); }
  .hero__dot--current { background: transparent; border: 1.5px solid var(--white); }

  .services { position: absolute; left: 0; top: 536px; width: 1200px; height: 114px; background: var(--white); }
  .service { position: absolute; top: -72px; width: 200px; text-align: center; }
  .service__icon {
    display: flex; align-items: center; justify-content: center;
    width: 116px; height: 116px; margin: 0 auto; border-radius: 50%;
    background: radial-gradient(circle at 38% 30%, var(--icon-blue) 0%, var(--icon-deep) 100%);
    box-shadow: 0 3px 8px rgba(10,40,90,0.25);
  }
  .service__label { margin-top: 6px; font-size: 16px; font-weight: 700; line-height: 21px; color: var(--ink); }

  .footer-band {
    position: absolute; left: 0; top: 650px; width: 1200px; height: 26px;
    background: linear-gradient(to right, var(--band-light) 0 448px, var(--band-mid) 448px 835px, var(--band-light) 835px);
  }
</style>
</head>
<body>

<header>
  <div class="top-bar">
    <span class="top-bar__tagline">Looking For A Great New Jersey IT Support Company?</span>
    <span class="top-bar__phone">
      <svg width="11" height="11" viewBox="0 0 24 24" aria-hidden="true"><path fill="#fff" d="M6.6 10.8a15.1 15.1 0 0 0 6.6 6.6l2.2-2.2a1 1 0 0 1 1-.25 11.4 11.4 0 0 0 3.6.57 1 1 0 0 1 1 1V20a1 1 0 0 1-1 1A17 17 0 0 1 3 4a1 1 0 0 1 1-1h3.5a1 1 0 0 1 1 1c0 1.25.2 2.450.57 3.57a1 1 0 0 1-.25 1z"/></svg>
      (973) 555-0148
    </span>
    <div class="top-bar__tools">
      <span class="social-dot" aria-label="Social link"></span>
      <span class="social-dot" aria-label="Social link"></span>
      <svg width="12" height="12" viewBox="0 0 24 24" aria-label="Search"><circle cx="10" cy="10" r="6.5" fill="none" stroke="#fff" stroke-width="3"/><line x1="15" y1="15" x2="21" y2="21" stroke="#fff" stroke-width="3" stroke-linecap="round"/></svg>
    </div>
  </div>

  <nav class="site-nav">
    <a class="site-nav__link site-nav__link--active" href="#" style="left:90px">HOME</a>
    <a class="site-nav__link" href="#" style="left:170px">ABOUT US</a>
    <a class="site-nav__link" href="#" style="left:282px">HOW CAN WE HELP ?</a>
    <a class="site-nav__link" href="#" style="left:740px">MEDIA</a>
    <a class="site-nav__link" href="#" style="left:822px">BLOG</a>
    <a class="site-nav__link" href="#" style="left:896px">CONTACT US</a>
    <a class="site-nav__signup" href="#">SIGN UP</a>
  </nav>

  <div class="logo-tab">
    <span class="logo-tab__mark"></span>
    <span class="logo-tab__name">Brightline Tech Partners</span>
  </div>
</header>

<main>
  <section class="hero">
    <div class="hero__globe" role="img" aria-label="Wireframe globe of connected network points"></div>
    <h1 class="hero__headline">Grow Your Business with Managed IT Services from Brightline Tech Partners</h1>
    <div class="hero__dots">
      <span class="hero__dot hero__dot--current"></span>
      <span class="hero__dot"></span>
      <span class="hero__dot"></span>
      <span class="hero__dot"></span>
    </div>
  </section>

  <section class="services">
    <div class="service" style="left:117px">
      <span class="service__icon" role="img" aria-label="Managed IT services icon: cube">
        <svg width="80" height="80" viewBox="0 0 80 80" aria-hidden="true">
          <circle cx="40" cy="40" r="34" fill="none" stroke="var(--icon-pale)" stroke-width="3"/>
          <path d="M40 18 L60 28 L60 52 L40 62 L20 52 L20 28 Z" fill="#3aa8ff"/>
          <path d="M40 18 L60 28 L40 38 L20 28 Z" fill="#bfe2ff"/>
          <path d="M40 38 L60 28 L60 52 L40 62 Z" fill="#1a6fd0"/>
        </svg>
      </span>
      <p class="service__label">Managed<br>IT Services</p>
    </div>
    <div class="service" style="left:397px">
      <span class="service__icon" role="img" aria-label="Cloud computing icon: upward arrow">
        <svg width="80" height="80" viewBox="0 0 80 80" aria-hidden="true">
          <path d="M40 14 L58 36 H47 V64 H33 V36 H22 Z" fill="#ffffff"/>
          <rect x="33" y="56" width="14" height="8" fill="var(--icon-pale)"/>
        </svg>
      </span>
      <p class="service__label">New Jersey<br>Cloud Computing</p>
    </div>
    <div class="service" style="left:666px">
      <span class="service__icon" role="img" aria-label="Data protection icon: padlock">
        <svg width="80" height="80" viewBox="0 0 80 80" aria-hidden="true">
          <path d="M28 36 V28 a12 12 0 0 1 24 0 V36" fill="none" stroke="#e8f3ff" stroke-width="6"/>
          <rect x="20" y="36" width="40" height="32" rx="4" fill="#3a8de0" stroke="#e8f3ff" stroke-width="2"/>
          <circle cx="40" cy="52" r="9" fill="#e8f3ff"/>
          <circle cx="40" cy="52" r="4" fill="#1565c8"/>
        </svg>
      </span>
      <p class="service__label">Protect Your<br>Business Data</p>
    </div>
    <div class="service" style="left:926px">
      <span class="service__icon" role="img" aria-label="Managed email icon: envelope">
        <svg width="80" height="80" viewBox="0 0 80 80" aria-hidden="true">
          <circle cx="40" cy="40" r="14" fill="#ffffff"/>
          <rect x="32" y="35" width="16" height="11" rx="1" fill="none" stroke="#1e88e5" stroke-width="2"/>
          <path d="M32 35 L40 42 L48 35" fill="none" stroke="#1e88e5" stroke-width="2"/>
        </svg>
      </span>
      <p class="service__label">Managed Email<br>Solutions</p>
    </div>
  </section>

  <div class="footer-band"></div>
</main>

</body>
</html>
```